Business Card Design

The Copper Lantern is a traditional English pub serving a vast range of beers and real ales. It has a very conservative oulook. Something classy would work well. We have an in-house logo. I'm thinking of good quality card in say cream with matching compliment slips and headed paper and envelopes

Industry/Entity Type

Conservative

Contact Information for Business Card

Copper Lantern Public House
58 Fenwick Row
Pinner
Middlesex
HA7 2RD
Martin D Hale - Proprietor
www.copperlanternbrook.co.uk
Tel: 020 8514 7392
Mobile; 077300 41857

Requirements
Must have
• Cl design essential. Black text.

2 sets of business cards required. one set must have my name - Martin D Hale - Proprietor and the second set should have - Louise Carver - General Manager

```html
<!DOCTYPE html>
<html lang="en">
<head>
<meta charset="utf-8">
<title>The Copper Lantern – Business Cards</title>
<link rel="stylesheet" href="https://fonts.googleapis.com/css2?family=Oswald:wght@400;500;600;700&display=swap">
<style>
  :root {
    --backdrop: #d6d6d6;
    --card: #fbfbfa;
    --ink: #262626;
    --ink-soft: #333333;
    --on-band: #f4f4f4;
  }
  * { margin: 0; padding: 0; box-sizing: border-box; }
  html, body {
    width: 1200px;
    height: 800px;
    overflow: hidden;
    background: var(--backdrop);
  }
  .stage {
    position: relative;
    width: 1200px;
    height: 800px;
    display: flex;
    align-items: center;
    justify-content: center;
    gap: 40px;
    font-family: 'Oswald', sans-serif;
    color: var(--ink);
  }
  .card {
    position: relative;
    width: 540px;
    height: 315px;
    background: var(--card);
    box-shadow: 0 2px 6px rgba(0,0,0,0.18);
    overflow: hidden;
  }

  /* Brand mark: name set in text with a plain circle */
  .brand {
    display: flex;
    align-items: center;
    justify-content: center;
    gap: 12px;
  }
  .brand__circle {
    width: 54px;
    height: 54px;
    border-radius: 50%;
    background: var(--ink);
    flex: none;
  }
  .brand__name {
    font-weight: 700;
    text-transform: uppercase;
    line-height: 0.95;
    letter-spacing: 1px;
    color: var(--ink);
  }

  /* Back of card */
  .card--back .brand {
    position: absolute;
    top: 58px;
    left: 0;
    right: 0;
    flex-direction: column;
    gap: 14px;
  }
  .card--back .brand__circle { width: 78px; height: 78px; }
  .card--back .brand__name {
    font-size: 34px;
    text-align: center;
  }
  .card--back .band {
    position: absolute;
    left: 0;
    right: 0;
    top: 248px;
    height: 30px;
    background: var(--ink);
  }

  /* Front of card */
  .holder {
    position: absolute;
    top: 26px;
    left: 0;
    right: 0;
    text-align: center;
  }
  .holder__name {
    font-size: 32px;
    font-weight: 600;
    text-transform: uppercase;
    line-height: 1.05;
    letter-spacing: 0.5px;
  }
  .holder__role {
    font-size: 15px;
    font-weight: 600;
    text-transform: uppercase;
    letter-spacing: 0.5px;
  }
  .card--front .brand {
    position: absolute;
    top: 112px;
    left: 0;
    right: 0;
  }
  .card--front .brand__name { font-size: 24px; }
  .address {
    position: absolute;
    top: 190px;
    left: 0;
    right: 0;
    text-align: center;
    font-size: 12.5px;
    font-weight: 500;
    text-transform: uppercase;
    color: var(--ink-soft);
    letter-spacing: 0.2px;
  }
  .contact-band {
    position: absolute;
    left: 0;
    right: 0;
    top: 212px;
    height: 28px;
    background: var(--ink);
    color: var(--on-band);
    display: flex;
    align-items: center;
    justify-content: center;
    gap: 12px;
    font-size: 13px;
    font-weight: 400;
    text-transform: uppercase;
    letter-spacing: 0.3px;
  }
  .contact-band__sep { font-size: 12px; }
  .card--front .band {
    position: absolute;
    left: 0;
    right: 0;
    top: 262px;
    height: 30px;
    background: var(--ink);
  }
</style>
</head>
<body>
  <main class="stage">
    <section class="card card--back" aria-label="Business card, back">
      <div class="brand">
        <span class="brand__circle"></span>
        <span class="brand__name">Copper<br>Lantern</span>
      </div>
      <div class="band"></div>
    </section>

    <section class="card card--front" aria-label="Business card, front">
      <header class="holder">
        <h1 class="holder__name">Martin D Hale</h1>
        <p class="holder__role">Proprietor</p>
      </header>
      <div class="brand">
        <span class="brand__circle"></span>
        <span class="brand__name">Copper Lantern</span>
      </div>
      <p class="address">Copper Lantern Public House 58 Fenwick Row Pinner Middlesex HA7 2RD</p>
      <div class="contact-band">
        <span class="contact-band__item">Tel: 020 8514 7392</span>
        <span class="contact-band__sep">&#10033;</span>
        <span class="contact-band__item">Mobile: 077300 41857</span>
      </div>
      <div class="band"></div>
    </section>
  </main>
</body>
</html>
```